Lavoie Roofing

Want a professional looking business card

Industry/Entity Type

Business

Contact Information for Business Card

Mark Lavoie ( Owner) mark@lavoieroofing.example, www.lavoieroofing.example, Adress: 4712 County road 31 Plantagenet,ON K0B2M4

```html
<!DOCTYPE html>
<html lang="en">
<head>
<meta charset="utf-8">
<title>Lavoie Roofing – Business Card</title>
<link rel="stylesheet" href="https://fonts.googleapis.com/css2?family=Roboto:wght@400;500;700&display=swap">
<style>
  :root {
    --backdrop: #e6e6e6;
    --card: #ffffff;
    --brand-blue: #1f4b94;
    --text-grey: #6b6b6b;
    --divider: #d6d6d6;
    --pattern-light: #f8f9fb;
    --pattern-tone: #e9edf4;
  }
  * { box-sizing: border-box; margin: 0; padding: 0; }
  html, body {
    width: 1200px; height: 1000px; overflow: hidden;
    background: var(--backdrop);
    font-family: "Roboto", Arial, sans-serif;
  }
  .canvas { position: relative; width: 1200px; height: 1000px; }
  .card {
    position: absolute; left: 269px; width: 662px; height: 378px;
    background: var(--card);
    box-shadow: 0 3px 6px rgba(0,0,0,0.25);
  }
  .card--front { top: 108px; }
  .card--back { top: 521px; }

  .front-pattern {
    position: absolute; inset: 0;
    background: radial-gradient(ellipse at center, var(--pattern-light) 0%, var(--pattern-light) 35%, var(--pattern-tone) 100%);
  }

  .brand {
    position: absolute;
    display: flex; align-items: center; justify-content: center;
    white-space: nowrap;
  }
  .brand__mark { background: var(--brand-blue); flex: none; }
  .brand__name {
    color: var(--brand-blue);
    font-weight: 700;
    letter-spacing: 1px;
    line-height: 1;
  }
  .card--front .brand { left: 0; right: 0; top: 160px; gap: 18px; }
  .card--front .brand__mark { width: 44px; height: 44px; }
  .card--front .brand__name { font-size: 50px; }

  .card--back .brand { left: 30px; width: 300px; top: 170px; gap: 12px; }
  .card--back .brand__mark { width: 28px; height: 28px; }
  .card--back .brand__name { font-size: 31px; }

  .divider {
    position: absolute; left: 331px; top: 107px; width: 1px; height: 168px;
    background: var(--divider);
  }
  .contact { position: absolute; left: 356px; top: 103px; color: var(--text-grey); }
  .contact__name { color: var(--brand-blue); font-size: 18px; font-weight: 500; line-height: 22px; }
  .contact__role { font-size: 14px; line-height: 20px; }
  .contact__address { margin-top: 16px; font-size: 15px; line-height: 21px; }
  .contact__list { list-style: none; margin-top: 11px; font-size: 15px; line-height: 21px; }
  .contact__list li { display: flex; align-items: center; gap: 5px; }
  .contact__list svg { width: 11px; height: 11px; fill: var(--brand-blue); flex: none; }
  .contact__highlight { color: var(--brand-blue); }
</style>
</head>
<body>
<div class="canvas">
  <section class="card card--front">
    <div class="front-pattern" role="img" aria-label="Faint repeating pattern of light house outlines covering the card"></div>
    <div class="brand">
      <span class="brand__mark"></span>
      <span class="brand__name">Lavoie Roofing</span>
    </div>
  </section>

  <section class="card card--back">
    <div class="brand">
      <span class="brand__mark"></span>
      <span class="brand__name">Lavoie Roofing</span>
    </div>
    <div class="divider"></div>
    <div class="contact">
      <div class="contact__name">Mark Lavoie</div>
      <div class="contact__role">Owner</div>
      <div class="contact__address">4712 County road 31 Plantagenet,<br>ON K0B2M4</div>
      <ul class="contact__list">
        <li>
          <svg viewBox="0 0 12 12" aria-hidden="true"><path d="M3 1l2 2.5-1.2 1.4a7 7 0 0 0 3.3 3.3L8.5 7 11 9l-1.5 2C5 11 1 7 1 2.5z"/></svg>
          (613) 555-0147
        </li>
        <li>
          <svg viewBox="0 0 12 12" aria-hidden="true"><path d="M0 2h12v1L6 7 0 3zM0 4.2l6 4 6-4V10H0z"/></svg>
          mark@lavoieroofing.example
        </li>
        <li>
          <svg viewBox="0 0 12 12" aria-hidden="true"><path d="M6 0a6 6 0 1 0 0 12A6 6 0 0 0 6 0zm0 1.2c.8.8 1.3 2.2 1.4 3.8H4.6C4.7 3.4 5.2 2 6 1.2zM1.2 6.8h2.2c.1 1.5.5 2.8 1.1 3.7A4.8 4.8 0 0 1 1.2 6.8zm0-1.6a4.8 4.8 0 0 1 3.3-3.7c-.6.9-1 2.2-1.1 3.7zm4.8 5.6c-.8-.8-1.300-2.2-1.4-4h2.8c-.1 1.8-.6 3.2-1.4 4zm1.5-.3c.6-.9 1-2.2 1.1-3.7h2.2a4.8 4.8 0 0 1-3.3 3.7zm1.1-5.3c-.1-1.5-.5-2.8-1.1-3.7a4.8 4.8 0 0 1 3.3 3.7z"/></svg>
          <span>www.<span class="contact__highlight">lavoieroofing</span>.example</span>
        </li>
      </ul>
    </div>
  </section>
</div>
</body>
</html>
```